Plumbing Van Vehicle Signage

I need a design for vehicle signage for a group of plumbing vans. The company name is 'Kestrel Gas & Plumbing'. I do all types of plumbing and gas fitting but specialise in general maintenance plumbing and gas fitting.

Industry/Entity Type

Plumbing

Requirements
Must have
• Must be eye catching. Must be able to go on a white back ground as the vans are white. Must contain phone number

```html
<!DOCTYPE html>
<html lang="en">
<head>
<meta charset="utf-8">
<title>Kestrel Gas &amp; Plumbing – Van Signage</title>
<link rel="stylesheet" href="https://fonts.googleapis.com/css2?family=Russo+One&family=Open+Sans:wght@700&display=swap">
<style>
  :root {
    --canvas: #eceef0;
    --van-white: #ffffff;
    --panel-edge: #d4d7db;
    --brand-blue: #1f5fb4;
    --charcoal: #333538;
    --band-dark: #34373a;
    --accent-yellow: #f6c21a;
    --flame-amber: #f5b01c;
    --flame-red: #e53f1c;
    --mark-grey: #6f7378;
  }
  html, body {
    margin: 0;
    padding: 0;
    width: 1200px;
    height: 1200px;
    overflow: hidden;
    background: var(--canvas);
  }
  .signage-sheet {
    display: block;
    width: 1200px;
    height: 1200px;
  }
  .side-panel { fill: var(--van-white); stroke: var(--panel-edge); stroke-width: 2; }
  .swoosh-fill { fill: url(#flameGradient); }
  .swoosh-band { fill: var(--band-dark); }
  .swoosh-edge { fill: var(--accent-yellow); }
  .brand-mark { fill: var(--mark-grey); }
  .phone-number {
    font-family: "Open Sans", sans-serif;
    font-weight: 700;
    font-size: 44px;
    fill: var(--charcoal);
    letter-spacing: 1px;
  }
  .brand-name {
    font-family: "Russo One", sans-serif;
    font-weight: 400;
    fill: var(--brand-blue);
  }
  .brand-name--primary { font-size: 116px; }
  .brand-name--secondary { font-size: 48px; letter-spacing: 2px; }
  .web-address {
    font-family: "Open Sans", sans-serif;
    font-weight: 700;
    font-size: 30px;
    fill: var(--van-white);
    letter-spacing: 1px;
  }
</style>
</head>
<body>
<svg class="signage-sheet" viewBox="0 0 1200 1200" xmlns="http://www.w3.org/2000/svg">
  <defs>
    <linearGradient id="flameGradient" x1="0" y1="0" x2="0" y2="1">
      <stop offset="0" stop-color="var(--flame-amber)"/>
      <stop offset="0.55" stop-color="#f08a1c"/>
      <stop offset="1" stop-color="var(--flame-red)"/>
    </linearGradient>
  </defs>

  <!-- Kerb side: cab to the right -->
  <g class="van-side van-side--kerb" transform="translate(50,70)">
    <rect class="side-panel" x="0" y="0" width="1100" height="480" rx="18"/>
    <polygon class="swoosh-fill" points="0,335 1100,465 1100,480 0,480"/>
    <polygon class="swoosh-edge" points="0,282 1100,412 1100,418 0,288"/>
    <polygon class="swoosh-band" points="0,290 1100,420 1100,465 0,335"/>
    <circle class="brand-mark" cx="140" cy="170" r="72"/>
    <text class="phone-number" x="290" y="150">555-014-2290</text>
    <text class="brand-name brand-name--primary" x="240" y="255">KESTREL</text>
    <text class="brand-name brand-name--secondary" x="320" y="310">GAS &amp; PLUMBING</text>
    <text class="web-address" x="560" y="389" text-anchor="middle" transform="rotate(6.74 560 378)">www.kestrelgasplumbing.com</text>
  </g>

  <!-- Driver side: cab to the left -->
  <g class="van-side van-side--driver" transform="translate(50,650)">
    <rect class="side-panel" x="0" y="0" width="1100" height="480" rx="18"/>
    <polygon class="swoosh-fill" points="0,465 1100,335 1100,480 0,480"/>
    <polygon class="swoosh-edge" points="0,412 1100,282 1100,288 0,418"/>
    <polygon class="swoosh-band" points="0,420 1100,290 1100,335 0,465"/>
    <circle class="brand-mark" cx="960" cy="170" r="72"/>
    <text class="phone-number" x="440" y="150">555-014-2290</text>
    <text class="brand-name brand-name--primary" x="230" y="255">KESTREL</text>
    <text class="brand-name brand-name--secondary" x="290" y="310">GAS &amp; PLUMBING</text>
    <text class="web-address" x="520" y="392" text-anchor="middle" transform="rotate(-6.74 520 381)">www.kestrelgasplumbing.com</text>
  </g>
</svg>
</body>
</html>
```